Looking for updated Letterhead and Compliments Slips to go with our new updated logo. This stationary will be used for letters to suppliers and customers so needs to be practical while also quite classic.

We are an engineering company so needs to be clean and precise

Target Market(s)

SME'S and large automotive customers

Industry/Entity Type

Automotive

Font styles to use
Sans Serif

Colors
85acd3
0356a4
0792cd
33a6d7
85abd2
ffffff

Requirements
Must have
• Address details as below
• KT Fabrications Limited
• Hallmere Road
• Rugby
• Warwickshire
• LP47 9XZ, UK
• Telephone: +44 (0)1632 960418
• Fax: +44 (0)1632 960733
• Email: sales@ktfabrications.example
• Web: www.ktfabrications.example
Nice to have
• Nice to have some element of being a British Manufacturer

```html
<!DOCTYPE html>
<html lang="en">
<head>
<meta charset="utf-8">
<title>KT Fabrications Letterhead</title>
<link rel="stylesheet" href="https://fonts.googleapis.com/css2?family=Lato:wght@400;700&display=swap">
<style>
  :root {
    --brand-blue: #0356a4;
    --brand-sky: #33a6d7;
    --brand-grey: #5b5d62;
    --ink: #2b2b2b;
    --ink-soft: #4a4a4a;
    --paper: #ffffff;
    --backdrop: #e6e6e6;
  }
  * { box-sizing: border-box; margin: 0; padding: 0; }
  html, body {
    width: 1200px; height: 1200px; overflow: hidden;
    background: var(--backdrop);
    font-family: "Lato", "Helvetica Neue", Arial, sans-serif;
    color: var(--ink);
  }
  .letterhead {
    position: absolute; left: 204px; top: 40px;
    width: 792px; height: 1120px;
    background: var(--paper);
    box-shadow: 0 4px 18px rgba(0,0,0,0.12);
    overflow: hidden;
  }
  .brand {
    position: absolute; left: 62px; top: 78px;
    display: flex; align-items: center; gap: 10px;
  }
  .brand-mark { width: 16px; height: 16px; background: var(--brand-blue); }
  .brand-name {
    font-size: 17px; font-weight: 700; letter-spacing: 4px;
    color: var(--brand-blue); text-transform: uppercase;
  }
  .contact {
    position: absolute; left: 520px; top: 56px;
    padding-left: 14px; border-left: 1px solid #6d6d6d;
    font-size: 9.5px; line-height: 1.5; color: var(--ink-soft);
  }
  .contact-row { display: flex; align-items: center; gap: 6px; }
  .contact-row svg { width: 9px; height: 9px; fill: var(--brand-blue); flex: none; }
  .contact-address { margin-bottom: 2px; }
  .letter-body {
    position: absolute; left: 62px; top: 210px; width: 600px;
    font-size: 13.5px; line-height: 1.62; color: var(--ink);
  }
  .salutation { font-size: 14px; margin-bottom: 18px; }
  .letter-body p { margin-bottom: 22px; }
  .signature {
    width: 90px; height: 48px; margin: 10px 0 8px 20px;
    background: linear-gradient(90deg, #ececec, #dcdcdc);
    border-radius: 4px;
  }
  .signatory-name { font-size: 19px; margin-left: 20px; }
  .signatory-role { font-size: 13px; color: var(--ink-soft); margin-left: 20px; }
  .footer-swoosh { position: absolute; left: 0; bottom: 0; width: 792px; height: 520px; }
</style>
</head>
<body>
  <main class="letterhead">
    <header class="brand">
      <span class="brand-mark"></span>
      <span class="brand-name">KT Fabrications</span>
    </header>

    <address class="contact">
      <div class="contact-address">Hallmere Road, Rugby,<br>Warwickshire, LP47 9XZ, UK</div>
      <div class="contact-row">
        <svg viewBox="0 0 10 10"><path d="M2 1l2 2-1 1.2c.6 1.2 1.6 2.2 2.8 2.8L7 6l2 2-1.2 1.2C4.5 9 1 5.5.8 2.2z"/></svg>
        +44 (0)1632 960418
      </div>
      <div class="contact-row">
        <svg viewBox="0 0 10 10"><rect x="2.5" y="1" width="5" height="3"/><rect x="1" y="4" width="8" height="4" rx="1"/></svg>
        +44 (0)1632 960733
      </div>
      <div class="contact-row">
        <svg viewBox="0 0 10 10"><path d="M1 2h8v6H1z M1 2l4 3 4-3" /></svg>
        sales@ktfabrications.example
      </div>
      <div class="contact-row">
        <svg viewBox="0 0 10 10"><circle cx="5" cy="5" r="4"/></svg>
        www.ktfabrications.example
      </div>
    </address>

    <section class="letter-body">
      <div class="salutation">Dear Mr. Carter,</div>
      <p>Lorem ipsum dolor sit amet, consectetur adipiscing elit. Donec orci purus, luctus vitae dignissim eu, iaculis sed purus. Vivamus faucibus, ipsum nec aliquet viverra, leo mauris condimentum ligula, sit amet sagittis enim ligula quis arcu. Nam egestas tortor id nisi porttitor mattis. In tortor ante, ultricies in suscipit a, tempus non massa. Vivamus et auctor mi. Fusce vel massa nulla. Phasellus nec eros mauris, et scelerisque orci. Donec malesuada orci vitae nulla accumsan porta a id massa. Quisque accumsan iaculis magna sit amet fringilla. Maecenas consequat, magna eget tincidunt semper, odio nibh rutrum mi, id feugiat ante nisi eu risus. Vestibulum nunc orci, rhoncus a placerat in, ultricies in mi. Cras mattis varius eros, vel fringilla nisi suscipit eget.</p>
      <p>Quisque scelerisque sagittis nulla at porttitor. Mauris a justo et tellus interdum tristique. Sed id augue vitae urna euismod commodo aliquet a quam. Pellentesque arcu velit, cursus et malesuada ut, consequat et diam. Nullam erat sem, rhoncus id ullamcorper vitae, rhoncus et arcu. In ultricies ultricies nulla, ut rutrum nisi iaculis at. Donec eu magna a metus ornare faucibus. Fusce aliquet faucibus ultricies. Morbi semper, est id tincidunt gravida, sem arcu adipiscing lacus, ac bibendum nulla leo eu purus. Quisque nec diam sed risus consectetur accumsan quis quis nibh. Vestibulum id purus lorem.</p>
      <div class="signature" role="img" aria-label="Handwritten signature of Daniel Hartley"></div>
      <div class="signatory-name">Daniel Hartley</div>
      <div class="signatory-role">Co-Founder &amp; CEO</div>
    </section>

    <svg class="footer-swoosh" viewBox="0 0 792 520" preserveAspectRatio="none" aria-hidden="true">
      <path d="M380 520 C 520 420, 680 330, 792 40 L792 78 C 690 350, 540 440, 400 520 Z" fill="var(--brand-grey)"/>
      <path d="M400 520 C 560 430, 700 330, 792 20 L792 520 Z" fill="var(--brand-blue)"/>
    </svg>
  </main>
</body>
</html>
```